Business Card Design For Bluepine Audio

Bluepine Audio is a small pro-audio company providing rental and install services for professional sound reinforcement. Focus is gigs (any gigs) needing high quality audio; from corporate to chamber music to hard hitting rock.

Bluepine Audio
Pro-audio for your gig ... spine-tingle grand
Corin Halsey
corin@bluepineaudio.com.au
0438 562 071

We need a business card design and an "drop-off"' larger card (eg. one third A4 size: 99mm wide x 210mm high) with more details.
Updates

Please note I've had limited internet access for last few days and for the next four.  The work so far looks great .. I'll provide some individual feedback on the designs now.  Great work, many thanks, love the creativity!

Corin

Industry/Entity Type

Business

```html
<!DOCTYPE html>
<html lang="en">
<head>
<meta charset="utf-8">
<title>Bluepine Audio – Business Card</title>
<link rel="stylesheet" href="https://fonts.googleapis.com/css2?family=Arimo:wght@700&display=swap">
<style>
  :root {
    --card-black: #050403;
    --amber-warm: #8a5518;
    --amber-deep: #3a230c;
    --type-white: #ffffff;
  }

  html, body {
    margin: 0;
    padding: 0;
    width: 1200px;
    height: 664px;
    overflow: hidden;
    background: var(--card-black);
  }

  .business-card {
    position: relative;
    width: 1200px;
    height: 664px;
    overflow: hidden;
    font-family: "Arimo", "Helvetica Neue", Arial, sans-serif;
    font-weight: 700;
    color: var(--type-white);
  }

  .mixer-photo {
    position: absolute;
    inset: 0;
    background: linear-gradient(100deg,
      var(--amber-warm) 0%,
      var(--amber-deep) 30%,
      var(--card-black) 60%);
  }

  .card-text {
    position: absolute;
    margin: 0;
    line-height: 1;
    white-space: nowrap;
  }

  .brand-name {
    left: 294px;
    top: 80px;
    font-size: 52px;
    line-height: 120px;
  }

  .brand-initial {
    font-size: 120px;
    letter-spacing: -3px;
  }

  .contact-person {
    left: 0;
    width: 1160px;
    top: 208px;
    text-align: center;
    font-size: 38px;
  }

  .tagline {
    left: 0;
    width: 1222px;
    top: 261px;
    text-align: center;
    font-size: 42px;
  }

  .email {
    right: 5px;
    top: 512px;
    font-size: 44px;
  }

  .phone {
    right: 27px;
    top: 558px;
    font-size: 49px;
    letter-spacing: 1px;
  }
</style>
</head>
<body>
  <main class="business-card">
    <div class="mixer-photo" role="img" aria-label="Low-light close-up photograph of a DJ mixer and turntable with warm amber glow"></div>

    <h1 class="card-text brand-name"><span class="brand-initial">B</span>luepine Audio</h1>
    <p class="card-text contact-person">Corin Halsey</p>
    <p class="card-text tagline">Pro-audio for your gig ... spine-tingle grand</p>
    <p class="card-text email">corin@bluepineaudio.com.au</p>
    <p class="card-text phone">0438 562 071</p>
  </main>
</body>
</html>
```